Redesign Current Website Into An Exciting Updated Design

We need to redesign the current website www.gleamvoucherhub.com We want an overall new look. We are rebranding so it will be a new logo and we would like to see new images as well so you cannot compare the old from the new.

You can use same exact content as on current url www.gleamvoucherhub.com

The website must be warm and inviting and fun yet professional and modern.

The website must also be designed with mobile in mind

The website must be warm and inviting yet professional and modern.

The website must also be designed with mobile in mind.

Target Market(s)

Consumers redeeming rewards

Industry/Entity Type

Promotional Reward Fullfillment

Coding

Coded - Design and coding required

Number of Pages Required

3 page

Requirements
Must have
• This website is a website where consumers come to redeem rewards they received from doing business with a company that offers these rewards. So the website should be very inviting.
Nice to have
• open
Should not have
• open

```html
<!DOCTYPE html>
<html lang="en">
<head>
<meta charset="utf-8">
<title>Gleam Voucher Hub – The Online Redemption System</title>
<link href="https://fonts.googleapis.com/css2?family=Roboto+Condensed:wght@700&family=Roboto:wght@400;500;700&display=swap" rel="stylesheet">
<style>
:root{
  --blue:#2b5e8e;
  --blue-dark:#1f4a73;
  --blue-soft:#9fc0e0;
  --footer:#2d6193;
  --ink:#2a2a2a;
  --tint:#eef3f9;
  --field:#e4e4e4;
  --star:#f0a93a;
  --grass:#8cc13b;
  --grass-light:#b5d95a;
  --white:#ffffff;
}
*{margin:0;padding:0;box-sizing:border-box}
html,body{width:1200px;height:3404px;overflow:hidden}
body{position:relative;background:var(--white);font-family:"Roboto",sans-serif;color:var(--ink)}
.abs{position:absolute}
.heading{font-family:"Roboto Condensed",sans-serif;font-weight:700;color:var(--blue);text-transform:uppercase;letter-spacing:.2px}
.btn{position:absolute;background:var(--blue);color:var(--white);font-weight:700;font-size:14px;display:flex;align-items:center;justify-content:center;text-transform:uppercase;border-radius:2px}
.framed{position:absolute;padding:2px 0 4px 8px;border-left:2px solid var(--blue);border-bottom:2px solid var(--blue)}
.framed::before{content:"";position:absolute;left:-2px;top:-12px;width:30px;height:2px;background:var(--blue)}
.framed::after{content:"";position:absolute;left:-2px;top:-12px;width:2px;height:12px;background:var(--blue)}

/* hero */
.hero{position:absolute;left:0;top:0;width:1200px;height:646px;background:linear-gradient(180deg,#eef4fb 0%,#e4eef8 60%,#dcebf6 100%);overflow:hidden}
.clouds{position:absolute;left:-60px;top:-40px;width:1320px;height:520px;background:
  radial-gradient(ellipse 260px 180px at 180px 300px,#fff 0%,rgba(255,255,255,0) 70%),
  radial-gradient(ellipse 320px 200px at 600px 120px,#fff 0%,rgba(255,255,255,0) 70%),
  radial-gradient(ellipse 280px 200px at 1100px 200px,#fff 0%,rgba(255,255,255,0) 70%)}
.hero-art{position:absolute;left:600px;top:160px;width:560px;height:420px;border-radius:40px;background:
  radial-gradient(ellipse 90px 130px at 130px 260px,#e86aa0 0%,rgba(232,106,160,0) 100%),
  radial-gradient(ellipse 120px 180px at 420px 220px,rgba(210,190,170,.7) 0%,rgba(210,190,170,0) 100%),
  radial-gradient(ellipse 260px 200px at 280px 260px,rgba(205,180,150,.45) 0%,rgba(205,180,150,0) 100%)}
.brand{position:absolute;left:100px;top:36px;width:110px;font-family:"Roboto Condensed",sans-serif;font-weight:700;color:var(--blue);font-size:21px;line-height:21px;text-transform:uppercase;padding-left:6px;border-left:2px solid var(--blue)}
.burger{position:absolute;left:1078px;top:48px;width:18px;height:14px;border-top:3px solid #222;border-bottom:3px solid #222}
.burger::after{content:"";position:absolute;left:0;top:2.5px;width:18px;height:3px;background:#222}
.hero-title{position:absolute;left:102px;top:222px;font-size:49px;line-height:56px}
.hero-text{position:absolute;left:104px;top:349px;width:390px;font-size:11.5px;line-height:20px;color:#222}

/* redeem bar */
.redeem{position:absolute;left:133px;top:612px;width:934px;height:106px;background:var(--white);border-left:5px solid var(--blue);box-shadow:0 3px 10px rgba(0,0,0,.12);border-radius:3px}
.redeem-label{position:absolute;left:30px;top:28px;font-size:18px;line-height:26px}
.field{position:absolute;top:30px;height:47px;background:var(--field);border-radius:2px;display:flex;align-items:center;padding-left:14px;font-size:14px;color:#555;gap:8px}
.field svg{flex:none}

/* promos */
.promo-copy{position:absolute;left:104px;top:847px;font-size:14.5px;line-height:23px;color:#333}
.card{position:absolute;width:198px;height:204px;background:var(--white);border:2px solid #eceef1;border-radius:3px;text-align:center}
.card h3{font-weight:700;color:var(--blue);font-size:19px;line-height:28px;margin-top:22px}
.card svg{display:block;margin:16px auto 0}
.card.active{background:linear-gradient(160deg,#4a7fb2,#2b5e8e);border-color:#2b5e8e}
.card.active h3{color:var(--white)}

/* testimonials */
.testi{position:absolute;left:0;top:1306px;width:1200px;height:748px;background:var(--tint)}
.tcard{position:absolute;width:316px;background:var(--white);border:2px solid #e2e6ec;border-radius:14px;text-align:center;padding:26px 22px 0;overflow:hidden}
.tcard.focus{border-color:var(--blue)}
.quote{font-family:Georgia,serif;font-weight:700;font-size:60px;line-height:44px;height:34px;color:#b9c4d1;letter-spacing:-6px}
.tcard p{font-size:13.8px;line-height:25px;color:#333;margin-top:10px}
.avatar{width:64px;height:64px;border-radius:50%;margin:20px auto 0;background:linear-gradient(135deg,#2f8a86,#b0583a)}
.who{font-size:16px;margin-top:12px;color:#222}
.who b{font-weight:700}
.stars{color:var(--star);font-size:11px;letter-spacing:1px;margin-top:4px}
.round{position:absolute;width:40px;height:40px;border-radius:50%;display:flex;align-items:center;justify-content:center}
.round.outline{border:1.5px solid var(--blue);background:var(--white)}
.round.solid{background:var(--blue)}

/* welcome */
.mist{position:absolute;left:0;top:2440px;width:1200px;height:340px;background:linear-gradient(180deg,rgba(232,240,248,0) 0%,#e6eef6 45%,rgba(255,255,255,0) 100%)}
.welcome-ring{position:absolute;left:104px;top:2128px;width:440px;height:450px;border-radius:55% 45% 48% 52% / 48% 50% 50% 52%;border:2px solid var(--blue);border-right-color:transparent;border-top-color:transparent}
.welcome-photo{position:absolute;left:116px;top:2136px;width:415px;height:432px;border-radius:58% 42% 48% 52% / 46% 50% 50% 54%;background:
  radial-gradient(ellipse 120px 150px at 200px 230px,#f0a62a 0%,rgba(240,166,42,0) 100%),
  linear-gradient(150deg,#6b5540 0%,#c98a3a 45%,#4d6f98 100%)}
.chip{position:absolute;width:58px;height:58px;background:var(--white);border-radius:8px;box-shadow:0 2px 8px rgba(0,0,0,.14);display:flex;align-items:center;justify-content:center}
.welcome-text{position:absolute;left:640px;top:2285px;width:440px;font-size:14px;line-height:24px;color:#333}

/* clients */
.logos{position:absolute;left:104px;top:2772px;width:988px;height:84px;border:1px solid #d8dce2;display:flex;background:var(--white)}
.logo-cell{flex:1;border-right:1px solid #d8dce2;display:flex;align-items:center;justify-content:center;gap:8px;font-weight:700;font-size:15px;color:#4a4f57}
.logo-cell:last-child{border-right:none}
.logo-cell.lift{box-shadow:0 4px 12px rgba(0,0,0,.18);position:relative;z-index:1}
.logo-cell i{width:12px;height:12px;border-radius:50%;background:#4a4f57;display:block}
.skyline{position:absolute;left:40px;top:2890px;width:1120px;height:198px;background:
  linear-gradient(180deg,rgba(236,240,244,0) 0%,#eceff2 55%,#f1e6d6 100%)}

/* footer */
.footer{position:absolute;left:0;top:3088px;width:1200px;height:316px;background:var(--footer);color:var(--white)}
.f-brand{position:absolute;left:120px;top:80px;width:170px;padding:14px;border:2px solid var(--white);font-family:"Roboto Condensed",sans-serif;font-weight:700;font-size:30px;line-height:32px;text-transform:uppercase}
.f-col{position:absolute;top:72px}
.f-col h4{font-family:"Roboto Condensed",sans-serif;font-weight:700;font-size:22px;text-transform:uppercase;margin-bottom:10px}
.f-col li{list-style:none;font-size:14px;line-height:28px}
.f-rule{position:absolute;left:104px;top:257px;width:990px;height:1px;background:rgba(255,255,255,.35)}
.f-copy{position:absolute;left:0;top:277px;width:1200px;text-align:center;font-size:14px}
</style>
</head>
<body>

<section class="hero">
  <div class="clouds"></div>
  <div class="hero-art" role="img" aria-label="Illustration of a giant gift box, travellers with luggage and world landmarks on a hill"></div>
  <svg class="abs" style="left:0;top:470px" width="1200" height="176" viewBox="0 0 1200 176" aria-hidden="true">
    <path d="M0 60 C 200 10, 420 30, 640 70 S 1000 40, 1200 30 L1200 176 L0 176 Z" fill="#b5d95a"/>
    <path d="M0 95 C 260 60, 520 80, 760 110 S 1060 90, 1200 80 L1200 176 L0 176 Z" fill="#8cc13b"/>
  </svg>
  <div class="brand">Gleam Voucher Hub</div>
  <div class="burger"></div>
  <h1 class="heading hero-title">The Online<br>Redemption System</h1>
  <p class="hero-text">To Learn More About Your Offer Including The Full Details, How It Works, Terms, FAQ's and To Redeem and Activate Your Certificate Please Enter A Valid Certificate Number and Email.</p>
  <div class="btn" style="left:104px;top:427px;width:216px;height:47px">Redeem Your Offer Now</div>
</section>

<div class="redeem">
  <div class="heading redeem-label">Redeem and Activate<br>Your Certificate</div>
  <div class="field" style="left:243px;width:247px">
    <svg width="16" height="16" viewBox="0 0 16 16"><rect x="2" y="1" width="12" height="14" fill="none" stroke="#555" stroke-width="1.3"/><path d="M5 5h6M5 8h6M5 11h4" stroke="#555" stroke-width="1.2"/></svg>
    Certificate_ID
  </div>
  <div class="field" style="left:501px;width:247px">
    <svg width="16" height="16" viewBox="0 0 16 16"><rect x="1.5" y="3.5" width="13" height="10" fill="none" stroke="#555" stroke-width="1.3"/><path d="M1.5 4l6.5 5 6.5-5" fill="none" stroke="#555" stroke-width="1.2"/></svg>
    Enter Email Address
  </div>
  <div class="btn" style="left:758px;top:30px;width:112px;height:47px">Submit</div>
</div>

<div class="framed" style="left:104px;top:790px">
  <h2 class="heading" style="font-size:33px;line-height:40px">Promos and Rewards</h2>
</div>
<p class="promo-copy">On every holiday,<br>shopping spree, dinner &amp; more.</p>
<div class="btn" style="left:104px;top:908px;width:216px;height:47px">Redeem Your Offer Now</div>

<div class="card" style="left:471px;top:799px"><h3>Vacation<br>Certificates</h3>
  <svg width="80" height="78" viewBox="0 0 80 78" aria-hidden="true">
    <rect x="6" y="4" width="44" height="62" rx="3" fill="#2b5e8e" stroke="#1b2c44" stroke-width="2"/>
    <circle cx="28" cy="26" r="11" fill="none" stroke="#fff" stroke-width="2"/>
    <path d="M17 26h22M28 15v22M21 19c4 4 10 4 14 0M21 33c4-4 10-4 14 0" stroke="#fff" stroke-width="1.5" fill="none"/>
    <rect x="34" y="36" width="40" height="30" rx="3" fill="#fff" stroke="#1b2c44" stroke-width="2"/>
    <circle cx="44" cy="47" r="4" fill="#9fc0e0"/><path d="M38 58c2-5 10-5 12 0" fill="#9fc0e0"/>
    <path d="M54 45h14M54 51h14M54 57h10" stroke="#1b2c44" stroke-width="2"/>
  </svg></div>
<div class="card" style="left:685px;top:799px"><h3>Travel<br>Vouchers</h3>
  <svg width="90" height="70" viewBox="0 0 90 70" aria-hidden="true">
    <rect x="10" y="10" width="74" height="46" rx="4" fill="#2b5e8e" transform="rotate(-8 47 33)"/>
    <rect x="4" y="16" width="74" height="46" rx="4" fill="#dfe6ee"/>
    <path d="M56 16v46" stroke="#9aa7b5" stroke-dasharray="3 3" stroke-width="1.5"/>
    <path d="M14 44l10-3 8-12 4 1-4 10 9-2 3-4 3 1-2 6 1 2-6 1-2 3-3-1 1-3-9 3-3 7-4 1 1-8-9 2z" fill="#2b5e8e"/>
    <path d="M62 30h10M62 38h10M62 46h8" stroke="#9aa7b5" stroke-width="2"/>
  </svg></div>
<div class="card" style="left:898px;top:799px"><h3>Digital Electronic<br>Products</h3>
  <svg width="84" height="80" viewBox="0 0 84 80" aria-hidden="true">
    <rect x="30" y="4" width="30" height="52" rx="5" fill="#fff" stroke="#2b5e8e" stroke-width="3"/>
    <circle cx="45" cy="26" r="9" fill="#9fc0e0"/>
    <rect x="10" y="44" width="16" height="24" rx="4" fill="#2b5e8e"/><rect x="13" y="48" width="10" height="16" rx="2" fill="#9fc0e0"/>
    <rect x="40" y="50" width="36" height="22" rx="3" fill="#2b5e8e"/><circle cx="58" cy="61" r="6" fill="#fff"/><circle cx="58" cy="61" r="3" fill="#1b2c44"/>
    <rect x="34" y="72" width="44" height="4" rx="2" fill="#f0b43a"/>
  </svg></div>
<div class="card" style="left:471px;top:1023px"><h3>Dining<br>Incentives</h3>
  <svg width="90" height="80" viewBox="0 0 90 80" aria-hidden="true">
    <circle cx="56" cy="34" r="24" fill="#cfe0f1"/>
    <path d="M16 44h60a30 30 0 0 1-60 0z" fill="#2b5e8e" transform="translate(0 -4)"/>
    <path d="M20 40a26 20 0 0 1 52 0z" fill="#9fc0e0"/>
    <circle cx="46" cy="18" r="3" fill="#2b5e8e"/>
    <path d="M46 62v8M34 72h24" stroke="#1b2c44" stroke-width="3"/>
    <circle cx="70" cy="64" r="7" fill="#fff" stroke="#2b5e8e" stroke-width="2"/><path d="M67 64l2 2 4-4" stroke="#2b5e8e" stroke-width="2" fill="none"/>
  </svg></div>
<div class="card active" style="left:685px;top:1023px"><h3>Gas &amp; Grocery<br>Rewards</h3>
  <svg width="90" height="80" viewBox="0 0 90 80" aria-hidden="true" fill="none" stroke="#fff" stroke-width="3" stroke-linejoin="round">
    <path d="M6 10h12l8 40h44l8-30H22"/>
    <path d="M28 28h48M30 38h42M40 20v30M52 20v30M64 20v30"/>
    <circle cx="34" cy="64" r="6"/><circle cx="64" cy="64" r="6"/>
    <path d="M46 14c0-6 8-8 10-2M60 10l4-6M70 12l6-4" stroke-width="2.5"/>
  </svg></div>

<section class="testi">
  <div class="framed" style="left:433px;top:82px">
    <h2 class="heading" style="font-size:33px;line-height:40px">Client's Testimonials</h2>
  </div>
  <div class="tcard" style="left:13px;top:175px;height:359px">
    <div class="quote">&ldquo;</div>
    <p>The trip to Vegas was the perfect getaway for my husband and I. The city that never stops. It has a little of everything from sight seeing to fun all-night options. We had a blast!!!"</p>
    <div class="avatar" role="img" aria-label="Customer photo"></div>
    <div class="who"><b>Daniel R.</b> Flagstaff, AZ</div>
    <div class="stars">★★★★★</div>
  </div>
  <div class="tcard focus" style="left:354px;top:175px;height:452px">
    <div class="quote">&ldquo;</div>
    <p>It was GREAT! I've always wanted to go to Vegas. Being able to stay right on the strip was great. I love that we were able to walk to a lot of the sites. The fountains at the Riviera Palms were AMAZING! I LOVED the atmosphere and the food. The whole experience was awesome. I would love to return.</p>
    <div class="avatar" style="background:linear-gradient(135deg,#7b4a2a,#e3c48a)" role="img" aria-label="Customer photo"></div>
    <div class="who"><b>Maria C.</b> Bay Springs. MS</div>
    <div class="stars">★★★★★</div>
  </div>
  <div class="tcard" style="left:694px;top:175px;height:359px">
    <div class="quote">&ldquo;</div>
    <p>Very good. Las Vegas was a dream trip. Would go again without a doubt. It's the best. The hotels, the streets, the Grand Canyon. Everything is very good!</p>
    <div class="avatar" style="margin-top:45px;background:linear-gradient(180deg,#1f3552,#c9883a)" role="img" aria-label="Customer photo"></div>
    <div class="who"><b>Grace A.</b> Orlando, FL</div>
    <div class="stars">★★★★★</div>
  </div>
  <div class="tcard" style="left:1034px;top:175px;height:359px;width:200px;opacity:.6">
    <div class="quote">&ldquo;</div>
    <p>"I was worried it was a vacation certificate but they put me at ease. Always responding to email</p>
    <div class="avatar" style="background:#dfe3e8;margin-top:30px" role="img" aria-label="Customer photo"></div>
    <div class="who"><b>Selena M.</b> Faunsdale</div>
    <div class="stars">★★★★★</div>
  </div>
  <div class="round outline" style="left:1023px;top:312px"><svg width="14" height="14" viewBox="0 0 14 14"><path d="M2 7h10M8 3l4 4-4 4" fill="none" stroke="#2b5e8e" stroke-width="1.8"/></svg></div>
  <div class="round solid" style="left:1023px;top:357px"><svg width="14" height="14" viewBox="0 0 14 14"><path d="M12 7H2M6 3L2 7l4 4" fill="none" stroke="#fff" stroke-width="1.8"/></svg></div>
</section>

<div class="mist" role="img" aria-label="Soft misty mountain backdrop"></div>
<div class="welcome-ring"></div>
<div class="welcome-photo" role="img" aria-label="Smiling woman looking at her phone"></div>
<svg class="abs" style="left:56px;top:2160px" width="520" height="220" viewBox="0 0 520 220" aria-hidden="true">
  <path d="M20 0l5 11 12 1-9 8 3 12-11-6-11 6 3-12-9-8 12-1z" fill="#f0b43a"/>
  <path d="M356 0l4 9 10 1-8 7 3 10-9-5-9 5 3-10-8-7 10-1z" fill="#f0b43a"/>
  <path d="M432 10l3 6 6 1-5 4 2 6-6-3-6 3 2-6-5-4 6-1z" fill="#e8604a"/>
</svg>
<div class="chip" style="left:117px;top:2180px">
  <svg width="32" height="32" viewBox="0 0 32 32" aria-hidden="true"><rect x="4" y="12" width="24" height="18" fill="#e8443a"/><rect x="2" y="8" width="28" height="6" fill="#f0b43a"/><rect x="14" y="8" width="4" height="22" fill="#f0b43a"/><path d="M16 8c-4-6-9-4-7 0M16 8c4-6 9-4 7 0" stroke="#f0b43a" stroke-width="2" fill="none"/></svg>
</div>
<div class="chip" style="left:470px;top:2194px">
  <svg width="34" height="30" viewBox="0 0 34 30" aria-hidden="true"><path d="M4 10a6 5 0 0 1 10-2a5 4 0 0 1 8 2" fill="#cfe0f1"/><path d="M2 20l12-3 8-10 4 1-4 8 8-2 2-3 3 1-2 5-6 2-16 5z" fill="#2b5e8e"/><path d="M4 26h26" stroke="#9fc0e0" stroke-width="2"/></svg>
</div>
<div class="chip" style="left:470px;top:2400px">
  <svg width="32" height="32" viewBox="0 0 32 32" aria-hidden="true"><rect x="10" y="2" width="14" height="24" rx="3" fill="#fff" stroke="#2b5e8e" stroke-width="2"/><circle cx="17" cy="12" r="4" fill="#9fc0e0"/><rect x="2" y="18" width="8" height="12" rx="2" fill="#2b5e8e"/><rect x="16" y="22" width="14" height="8" rx="2" fill="#e86aa0"/></svg>
</div>

<div class="framed" style="left:641px;top:2198px">
  <h2 class="heading" style="font-size:33px;line-height:42px">Welcome to Gleam<br>Voucher Hub</h2>
</div>
<p class="welcome-text">We provide marketing incentives in the form of gift certificates and vouchers that are redeemable for a variety of items such as: discount travel, smart device products, restaurant incentives , golf discounts and more to thousands of businesses around the world who use them to create exciting marketing promotions and giveaways, customer loyalty programs, promotional contests and use them as customer appreciation gifts.</p>
<div class="btn" style="left:641px;top:2472px;width:128px;height:46px">Read More</div>

<div class="framed" style="left:508px;top:2677px">
  <h2 class="heading" style="font-size:33px;line-height:40px">Our Clients</h2>
</div>
<div class="logos">
  <div class="logo-cell"><i></i>Harborline Mutual</div>
  <div class="logo-cell">Meadowgate Insurance</div>
  <div class="logo-cell lift">Corevia Health</div>
  <div class="logo-cell">Brightkey Realty</div>
  <div class="logo-cell"><i></i>Roamwide Travel</div>
</div>
<div class="round solid" style="left:35px;top:2793px"><svg width="14" height="14" viewBox="0 0 14 14"><path d="M12 7H2M6 3L2 7l4 4" fill="none" stroke="#fff" stroke-width="1.8"/></svg></div>
<div class="round outline" style="left:1133px;top:2817px"><svg width="14" height="14" viewBox="0 0 14 14"><path d="M2 7h10M8 3l4 4-4 4" fill="none" stroke="#2b5e8e" stroke-width="1.8"/></svg></div>
<div class="skyline" role="img" aria-label="Faint illustration of world landmarks skyline"></div>

<footer class="footer">
  <div class="f-brand">Gleam Voucher Hub</div>
  <div class="f-col" style="left:385px"><h4>Quick Links</h4><ul><li>Home</li><li>About Us</li><li>Testimonials</li><li>Contact Us</li></ul></div>
  <div class="f-col" style="left:578px"><h4>Conatct Us</h4><ul><li style="line-height:22px;margin:3px 0">25, Gleamvoucher Lane<br>Lorem ipsum&nbsp; USA</li><li>+1 888 888 8888</li><li>info@gleamvoucherhub.com</li></ul></div>
  <div class="f-col" style="left:863px"><h4>Help Links</h4><ul><li>Privacy Policy</li><li>Terms Of Use</li><li>Already Redeemed?</li><li>Help</li></ul></div>
  <div class="f-rule"></div>
  <div class="f-copy">© 2025 Gleam Voucher Hub | All rights reserved</div>
</footer>

</body>
</html>
```